Dry Cleaners Pick-up & Delivery Service

We are in the need of a post card design to hand out in public focused in our dry-cleaners pick up and delivery business services. The postcard must include a price list of most common items sent to the dry cleaners on a regular basis along with promotional sign-up deals and specials as advertised on our website. The color palette must match our website's color scheme - www.vorqualin.com - we would like to focus on our free pick-up and free delivery service. The hand out post card should look clean, organized and neat, yet modern in style projecting the cleanliness of the clothing articles that our customer let us take care of saving them time while we take care of this errand for them. All new customers receive a free high quality, heavy duty laundry bag with our business information and are encouraged to request for $10 of free dry cleaning on their first order, no strings attached, just for signing up to our service.We strive to please our customers and invest on them to have more free time on their hands, plain and simple. We also offer law enforcement uniform special, as the area we focus our routes is a high law enforcement residential community. The logo is attached and must be visible in the postcard as well as the website address and phone number 305-472-1946 as these are the main contact forms of clients reaching our business. This is home based business, we have a partnership with a dry cleaners business who does all of our route customers' dry cleaning needs. Our business is all about the marketing, sales and networking with corporate businesses. The postcard handout must have designs of both sides of the post card as well. They will not be used for mailing for the moment being, they will be only used to hand out.

Industry/Entity Type

Dry Cleaning

```html
<!DOCTYPE html>
<html lang="en">
<head>
<meta charset="utf-8">
<title>Vorqualin – Dry Cleaners Pick-up &amp; Delivery Postcard</title>
<link rel="stylesheet" href="https://fonts.googleapis.com/css2?family=Nunito:wght@700;800;900&family=Oswald:wght@300;400&family=Anton&family=Open+Sans:wght@400;600&display=swap">
<style>
  :root {
    --page: #e4e5e7;
    --blue-deep: #0a4fa6;
    --blue: #1577cf;
    --blue-light: #3aa3ea;
    --blue-pale: #8fcdf4;
    --green: #8cc63f;
    --green-dark: #5f9a1d;
    --red: #d21f26;
    --ink: #111111;
    --white: #ffffff;
  }
  * { box-sizing: border-box; margin: 0; padding: 0; }
  html, body { width: 772px; height: 1200px; overflow: hidden; }
  body { background: var(--page); position: relative; font-family: "Open Sans", sans-serif; }

  .card { position: absolute; left: 36px; width: 700px; height: 536px; overflow: hidden; box-shadow: 0 6px 16px rgba(0,0,0,.25); }
  .card--front { top: 30px; background: linear-gradient(135deg, var(--blue-light) 0%, var(--blue) 45%, var(--blue-deep) 100%); }
  .card--back { top: 618px; background: var(--blue); }

  /* ---------- Front ---------- */
  .front-photo { position: absolute; left: 0; top: 0; width: 350px; height: 470px;
    background: linear-gradient(160deg, #d9c79a 0%, #eef1f6 30%, #b8c8e6 55%, #e9edf5 80%, #9fb0d4 100%); }
  .front-wave { position: absolute; left: 0; top: 380px; width: 700px; height: 156px; }
  .badge { position: absolute; border-radius: 50%; display: flex; align-items: center; justify-content: center; text-align: center;
    font-family: "Nunito", sans-serif; font-weight: 800; color: var(--white); border: 4px solid var(--white); }
  .badge--care { left: 40px; top: 4px; width: 180px; height: 180px; background: radial-gradient(circle at 40% 35%, #a8d85a, var(--green-dark));
    font-size: 20px; line-height: 1.5; }
  .badge--offer { left: 168px; top: 317px; width: 180px; height: 180px; background: radial-gradient(circle at 40% 35%, #ee3a3f, #a50f14);
    font-size: 19px; line-height: 1.25; }
  .badge--offer .big { font-size: 31px; display: block; }
  .photo-circle { position: absolute; border-radius: 50%; border: 4px solid var(--white); box-shadow: 0 3px 8px rgba(0,0,0,.3); }
  .photo-circle--basket { left: 21px; top: 344px; width: 134px; height: 134px; background: radial-gradient(circle, #b98a4f 0%, #8d5f30 55%, #d7d7d7 100%); }
  .photo-circle--towels { left: 357px; top: 256px; width: 136px; height: 136px; background: linear-gradient(180deg, #e0517a 0%, #2c3d8f 40%, #c02c4c 70%, #5f2a6e 100%); }
  .photo-circle--washer { left: 512px; top: 228px; width: 150px; height: 150px; background: radial-gradient(circle at 45% 50%, #f07a1e 0%, #6a3fb0 40%, #3a6fd0 70%, #f1f1f1 90%); }

  .front-copy { position: absolute; left: 371px; top: 28px; color: var(--white); font-family: "Nunito", sans-serif; font-weight: 900; }
  .front-copy .signup { font-size: 27px; line-height: 34px; }
  .front-copy .call { font-size: 24px; font-weight: 700; line-height: 40px; }
  .front-copy .call strong { font-size: 31px; font-weight: 900; }
  .front-copy .perks { font-size: 25px; line-height: 34px; margin-top: 20px; }

  .brand { position: absolute; display: flex; align-items: center; gap: 8px; font-family: "Nunito", sans-serif; font-weight: 800; }
  .brand .dot { width: 16px; height: 16px; border-radius: 50%; background: var(--green); }
  .brand--front { left: 440px; top: 425px; font-size: 34px; color: var(--green); }
  .tagline { position: absolute; font-family: "Nunito", sans-serif; font-weight: 700; font-size: 13px; }
  .tagline--front { left: 420px; top: 481px; color: var(--white); }
  .footer { position: absolute; left: 0; width: 700px; text-align: center; font-size: 15px; }
  .footer--front { top: 505px; color: var(--white); }
  .stripe { position: absolute; left: 0; bottom: 0; width: 700px; height: 5px; background: var(--green); }

  /* ---------- Back ---------- */
  .price-panel { position: absolute; left: 0; top: 0; width: 373px; height: 536px; background: var(--green); }
  .price-col { position: absolute; font-family: "Oswald", sans-serif; font-weight: 300; font-size: 11px; line-height: 1.18; color: var(--ink); }
  .price-col--a { left: 22px; top: 30px; width: 164px; }
  .price-col--b { left: 201px; top: 34px; width: 157px; }
  .price-col--c { left: 391px; top: 28px; width: 140px; }
  .price-col--d { left: 550px; top: 46px; width: 140px; }
  .divider { position: absolute; top: 30px; width: 0; border-left: 2px dotted rgba(255,255,255,.85); }
  .divider--green { left: 190px; height: 360px; }
  .divider--blue { left: 538px; height: 330px; }
  .section-title { font-family: "Anton", sans-serif; font-size: 19px; line-height: 1.05; color: var(--ink);
    text-shadow: -1px -1px 0 var(--white), 1px -1px 0 var(--white), -1px 1px 0 var(--white), 1px 1px 0 var(--white); }
  .item { display: flex; justify-content: space-between; gap: 6px; margin-top: 8px; }
  .item:first-of-type { margin-top: 0; }
  .item .price { font-weight: 400; font-size: 12px; white-space: nowrap; }
  .item .note { display: block; font-size: 10px; }
  .special-price { font-weight: 400; font-size: 12px; }
  .fine { font-size: 10px; margin-top: 10px; }
  .fine + .fine { margin-top: 2px; }
  .price-col--c .section-title.misc { margin-top: 14px; }
  .bubble { position: absolute; left: 530px; top: 136px; width: 200px; height: 160px; border-radius: 50%; background: var(--blue-pale); }
  .bubble-text { position: absolute; left: 568px; top: 150px; width: 120px; font-family: "Oswald", sans-serif; font-weight: 300; font-size: 11px; line-height: 1.3; text-align: justify; color: var(--ink); }
  .wash-fold { position: absolute; left: 550px; top: 310px; width: 140px; font-family: "Oswald", sans-serif; font-weight: 300; font-size: 11px; line-height: 1.18; }
  .back-wave { position: absolute; left: 0; top: 0; width: 700px; height: 536px; }
  .photo-circle--clothes { left: 252px; top: 360px; width: 116px; height: 116px; background: radial-gradient(circle at 50% 45%, #f0a3b8 0%, #d4207a 45%, #3e5fae 80%, #f0f0f0 100%); }
  .brand--back { left: 66px; top: 438px; font-size: 28px; color: var(--green-dark); }
  .tagline--back { left: 66px; top: 483px; color: var(--ink); font-size: 12px; }
  .footer--back { top: 506px; color: var(--blue); font-size: 15px; }
</style>
</head>
<body>

<section class="card card--front" aria-label="Postcard front">
  <div class="front-photo" role="img" aria-label="Close-up photo of folded striped dress shirts"></div>
  <svg class="front-wave" viewBox="0 0 700 156" aria-hidden="true">
    <path d="M0 110 C180 70 380 90 520 100 C600 106 660 98 700 88 L700 156 L0 156 Z" fill="#0d5fb8"/>
    <path d="M0 110 C180 70 380 90 520 100 C600 106 660 98 700 88" fill="none" stroke="#8cc63f" stroke-width="4"/>
  </svg>

  <div class="badge badge--care">Let us take care<br>of you and your<br>precious items!</div>
  <div class="photo-circle photo-circle--basket" role="img" aria-label="Photo of a wicker laundry basket full of clothes"></div>
  <div class="badge badge--offer"><span>Ask about<br>getting<span class="big">$10 off</span>your first<br>dry-cleaning<br>order!</span></div>
  <div class="photo-circle photo-circle--towels" role="img" aria-label="Photo of a stack of colourful folded towels"></div>
  <div class="photo-circle photo-circle--washer" role="img" aria-label="Photo of clothes spinning inside a washing machine drum"></div>

  <div class="front-copy">
    <p class="signup">Sign-up free!</p>
    <p class="call">Call <strong>305-472-1946</strong></p>
    <p class="perks">Free pick-up!<br>Free delivery!<br>Next-day service<br>available!</p>
  </div>

  <div class="brand brand--front"><span class="dot"></span>Vorqualin</div>
  <p class="tagline tagline--front">Dry Cleaners Pick-up &amp; Delivery Services, LLC</p>
  <p class="footer footer--front">2275 NW 84th Ave Miami FL 33172 us &nbsp;|&nbsp; 305-472-1946 &nbsp;|&nbsp; deliveryservice@vorqualin.com</p>
  <div class="stripe"></div>
</section>

<section class="card card--back" aria-label="Postcard back">
  <div class="price-panel"></div>
  <div class="divider divider--green"></div>
  <div class="divider divider--blue"></div>
  <div class="bubble"></div>

  <div class="price-col price-col--a">
    <h2 class="section-title">Dry Cleaning<br>Pricing</h2>
    <div class="item"><span>Women Dress<span class="note">Dry-Cleaned and Pressed –<br>Subject to surcharge (beads, etc.)</span></span><span class="price">$10.95</span></div>
    <div class="item"><span>Women Blouse<span class="note">Dry-Cleaned and Pressed</span></span><span class="price">$4.95</span></div>
    <div class="item" style="margin-top:2px"><span>Women Casual Pants/Jeans<span class="note">Dry-Cleaned &amp; Pressed –<br>Subject to surcharge (beads, etc.)</span></span><span class="price">$4.95</span></div>
    <div class="item"><span>Skirt - Long<span class="note">Dry-Cleaned &amp; Pressed</span></span><span class="price">$6.49</span></div>
    <div class="item"><span>Skirt - Short<span class="note">Dry-Cleaned &amp; Pressed</span></span><span class="price">$4.95</span></div>
    <div class="item"><span>Women Suit<span class="note">2 piece – Dry-Cleaned &amp; Pressed</span></span><span class="price">$10.95</span></div>
    <div class="item"><span>Women Evening/Formal Dress –<span class="note">From:<br>Subject to surcharge (beads, etc)</span></span><span class="price">$28.99</span></div>
    <div class="item"><span>Men's Shirt (100% cotton)<span class="note">Laundered &amp; Pressed</span></span><span class="price">$2.99</span></div>
    <div class="item"><span>Men Business Shirt</span><span class="price">$4.5</span></div>
  </div>

  <div class="price-col price-col--b">
    <div class="item"><span>Dry-Cleaned &amp; Pressed</span></div>
    <div class="item" style="margin-top:12px"><span>Men Business Pants<span class="note">Dry-Cleaned &amp; Pressed</span></span><span class="price">$4.95</span></div>
    <div class="item" style="margin-top:12px"><span>Men Business Vest<span class="note">Dry-Cleaned &amp; Pressed</span></span><span class="price">$4.95</span></div>
    <div class="item" style="margin-top:12px"><span>Men Pants/Jeans<span class="note">Dry-Cleaned &amp; Pressed</span></span><span class="price">$4.95</span></div>
    <div class="item" style="margin-top:12px"><span>Men Suit<span class="note">2-Piece – Dry-Cleaned &amp; Pressed</span></span><span class="price">$10.95</span></div>
    <div class="item" style="margin-top:12px"><span>3 piece suit<span class="note">Dry-Cleaned &amp; Pressed</span></span><span class="price">$15.95</span></div>
    <div class="item" style="margin-top:12px"><span>Tie<span class="note">Dry-Cleaned &amp; Pressed</span></span><span class="price">$3.95</span></div>
    <div class="item" style="margin-top:12px"><span>Sports Coat/Jacket<span class="note">Dry-Cleaned &amp; Pressed</span></span><span class="price">$6.95</span></div>
    <div class="item" style="margin-top:12px"><span>Men Guayabera<span class="note">Laundered and Pressed</span></span><span class="price">$6.99</span></div>
  </div>

  <div class="price-col price-col--c">
    <h2 class="section-title">LAW<br>ENFORCEMENT<br>SPECIAL</h2>
    <p class="special-price">$7.99</p>
    <p class="fine" style="font-size:11px">1 LEO shirt with 1 LEO pair of<br>pants Dry-Cleaned and Pressed</p>
    <p class="fine" style="margin-top:22px">*Items that are silk, linen or lint are subject to a surcharge of up to $3.00 for each of those items in your order.</p>
    <p class="fine">*Items that have beads or garments with attached accessories are subject to a surcharge of up to $4.00 for each garment in your order with such attachments. Varies depending on the volume attached to the garment.</p>
    <h2 class="section-title misc">Miscellaneous<br>Items Pricing</h2>
    <div class="item" style="margin-top:14px"><span>Pillow Covers<span class="note">Any size</span></span><span class="price">$2.99</span></div>
    <div class="item" style="margin-top:14px"><span>Table Cloths &amp; Runners (Large)<span class="note">$11.95</span></span></div>
  </div>

  <div class="price-col price-col--d">
    <div class="item"><span>Table Cloth &amp; Runners (Small)<span class="note">$9.99</span></span></div>
    <div class="item" style="margin-top:14px"><span>Area Rugs – From:</span><span class="price">$24.95</span></div>
    <div class="item" style="margin-top:14px"><span>Subject to size –<span class="note">Ask for a quote</span></span></div>
  </div>

  <p class="bubble-text">We also pick up and deliver bed sheets, quilts, comforters, area rugs, etc. Price will be determined by the size of the item. Please inquire if you need to have these items dry-cleaned or laundered and pressed.</p>

  <div class="wash-fold">
    <h2 class="section-title">Wash &amp; Fold<br>Pricing</h2>
    <p>Regular Clothing Articles<br>$1.99</p>
    <p class="fine" style="margin-top:16px">*Price displayed is per pound<br>Laundered and Pressed</p>
  </div>

  <svg class="back-wave" viewBox="0 0 700 536" aria-hidden="true">
    <path d="M0 405 C150 395 300 430 420 470 C520 500 620 480 700 455 L700 536 L0 536 Z" fill="#ffffff"/>
  </svg>
  <div class="photo-circle photo-circle--clothes" role="img" aria-label="Photo of hands holding a pile of colourful garments"></div>

  <div class="brand brand--back"><span class="dot"></span>Vorqualin</div>
  <p class="tagline tagline--back">Dry Cleaners Pick-up &amp; Delivery Services, LLC</p>
  <p class="footer footer--back">2275 NW 84th Ave Miami FL 33172 us &nbsp;|&nbsp; 305-472-1946 &nbsp;|&nbsp; deliveryservice@vorqualin.com</p>
  <div class="stripe"></div>
</section>

</body>
</html>
```